Business Card Design Project - Small Bar

We would like a design for a business card for our new small bar in Melbourne. It is quite the 'hipster' bar and the card would need to reflect this in its design. We do have a logo which needs to be used in the card, tho how it is incorporated is up to you! :)

OK, the Bar currently has a common 'inner city' vibe, i.e. random artwork, older 30s/40's club furniture, grafitti murals on the walls, eclectic objects etc etc Current clientele would be described as "hipster", "urban professional" etc. How to describe... they are 30, have a good job but have beards, beanies and own vinyl records. :)

The card will be used to give to professional contacts and to bands/solo artists we come across to invite them to come play at our venue, so somehow I would like it to convey the image of 'professional' and 'funky' all in one. Difficult I know.

I have asked for some advice on making this brief clearer, so check back.

Thanks all in advance. :)
Updates

Sorry all

I've now been told that it is WEST MELBOURNE 3003. Apparently we are on the border and it is referred to by either west or north Melbourne, but it is definitely West Melbourne 3003.

Things you learn hey? :)

Target Market(s)

Hipsters, urbanites, the inner city crowd

Industry/Entity Type

Artists

Requirements
Must have
• Logo (JPG file attached)
Name of the bar "The Lantern & Otter"
Address - 742 Brindle St, North Melbourne, Victoria 3051
Names - Owen Partridge, Lewis Dunhurst
mobile. 0417265093 and 0456302714
Obviously we would need separate cards?
Nice to have
• Facebook link
Facebook 'like' icon
Should not have
• traditional designs. I am looking for something unique and funky. with FUNK! :)

```html
<!DOCTYPE html>
<html lang="en">
<head>
<meta charset="utf-8">
<title>The Lantern &amp; Otter – Business Card</title>
<link rel="stylesheet" href="https://fonts.googleapis.com/css2?family=Arimo:wght@700&display=swap">
<style>
  :root {
    --band: #7f0032;
    --text: #ffffff;
    --vinyl-dark: #1c1a33;
    --vinyl-mid: #3b3760;
    --vinyl-light: #a9a4d6;
    --paint-yellow: #d8c97a;
  }
  * { margin: 0; padding: 0; box-sizing: border-box; }
  html, body {
    width: 1200px; height: 734px; overflow: hidden; background: #ffffff;
  }
  .card {
    position: relative; width: 1200px; height: 734px; overflow: hidden;
  }
  .record-artwork {
    position: absolute; inset: 0;
    background:
      radial-gradient(ellipse 260px 160px at 60px 40px, var(--paint-yellow), transparent 70%),
      radial-gradient(ellipse 300px 200px at 560px 130px, rgba(138,154,44,0.75), transparent 70%),
      radial-gradient(ellipse 260px 180px at 860px 110px, rgba(120,150,40,0.65), transparent 70%),
      radial-gradient(ellipse 340px 140px at 470px 390px, rgba(190,180,225,0.8), transparent 70%),
      radial-gradient(ellipse 200px 110px at 120px 410px, rgba(216,201,122,0.55), transparent 70%),
      radial-gradient(ellipse 240px 120px at 1120px 60px, rgba(176,122,142,0.6), transparent 70%),
      radial-gradient(ellipse 500px 260px at 700px 330px, var(--vinyl-light), transparent 75%),
      linear-gradient(160deg, var(--vinyl-dark) 0%, var(--vinyl-mid) 45%, #6c6894 70%, var(--vinyl-dark) 100%);
  }
  .info-band {
    position: absolute; left: 0; top: 468px; width: 1200px; height: 230px;
    background: var(--band);
  }
  .brand-mark {
    position: absolute; left: 22px; top: 30px; width: 150px; height: 170px;
    display: flex; flex-direction: column; justify-content: center; align-items: center;
    font-family: "Arimo", Arial, sans-serif; font-weight: 700;
    font-size: 22px; line-height: 1.2; color: var(--text); text-align: center;
  }
  .bar-name, .contact-name, .contact-line, .social-link {
    position: absolute; left: 0; width: 1200px;
    font-family: "Arimo", Arial, sans-serif; font-weight: 700;
    color: var(--text); text-align: center; line-height: 1.1;
  }
  .bar-name { top: 30px; font-size: 50px; letter-spacing: 0.5px; padding-left: 0; }
  .contact-name { top: 98px; font-size: 38px; letter-spacing: -0.5px; }
  .contact-line { top: 146px; font-size: 26px; letter-spacing: -0.3px; padding-left: 4px; }
  .social-link { top: 184px; font-size: 24px; letter-spacing: -0.3px; }
</style>
</head>
<body>
  <div class="card">
    <div class="record-artwork" role="img" aria-label="Close-up photograph of a vinyl record spinning under a turntable stylus, overlaid with loose splashes of green, yellow and violet paint"></div>
    <section class="info-band">
      <div class="brand-mark">The<br>Lantern<br>&amp; Otter</div>
      <h1 class="bar-name">The Lantern &amp; Otter</h1>
      <p class="contact-name">OWEN PARTRIDGE</p>
      <p class="contact-line">T: 0417265093 742 BRINDLE ST, WEST MELBOURNE, VICTORIA 3003</p>
      <p class="social-link">www.socialpage.com/pages/thelanternandotter</p>
    </section>
  </div>
</body>
</html>
```